Business Card Design Project

Use newly designed logo and tie into newly designed website
I need a new logo and website layout designed for my partner's business. This is a birthday present. His business is interior painting, wallpapering and design. He also has access to a wide variety of products including carpet, fabrics, furniture, wallpaper, tile, countertops, etc. I have attached some screen shots of his website for reference. He is a one man shop and has a stellar reputation with his customers. He is on-time, very tidy, excellent with animals, and always finishes on time and on budget. There are no restrictions on colors or fonts. The logo needs to work well with the website, business cards and printed materials. The website needs to flow content for device size so it looks just as good on a cell phone or tablet as it does on a desktop computer. Whatever the heck that's called!Thanks. I am looking forward to seeing everyone's ideas.
Updates
Hi Designers,
We've reopened this project as our logo design project has just completed.
Please refer to the uploaded files and make use of either Horizontal or Vertical versions of the logo depending on what you think is suitable for your design proposals.
We look forward to your creative submissions!
Target Market(s)
Consumers looking to improve the interior environment of their homes by updating wall paint or paper, flooring (either carpet, tile, or hardwoods), counter tops, window treatments, etc. Clients tend to be more upper middle class and have certain taste levels and expectations. New logo, website and business card should align to meet those levels.
Industry/Entity Type
Cell Phone
Look and feel
Each slider illustrates characteristics of the customer's brand and the style your logo design should communicate.

```html
<!DOCTYPE html>
<html lang="en">
<head>
<meta charset="utf-8">
<title>Merriwell Interior Designs – Business Card</title>
<link rel="stylesheet" href="https://fonts.googleapis.com/css2?family=Cinzel:wght@500;700&family=Crimson+Text:wght@400&display=swap">
<style>
  :root {
    --stage: #e9e9eb;
    --card: #ffffff;
    --navy: #2b2250;
    --tan: #b39a64;
    --orange: #f39a1f;
    --brick: #8e2a22;
    --ghost-light: #f4f4f4;
    --ghost-dark: #e4e4e4;
    --ink-light: #ffffff;
  }
  * { box-sizing: border-box; margin: 0; padding: 0; }
  html, body {
    width: 1200px; height: 780px; overflow: hidden;
    background: var(--stage);
  }
  .card {
    position: absolute; left: 75px; top: 90px;
    width: 1050px; height: 600px;
    background: var(--card);
    box-shadow: 0 6px 24px rgba(0,0,0,0.12);
    overflow: hidden;
  }
  .room-backdrop {
    position: absolute; left: 60px; top: 0;
    width: 690px; height: 600px;
    background: linear-gradient(160deg, var(--ghost-light) 0%, var(--ghost-dark) 55%, var(--ghost-light) 100%);
  }
  .brand {
    position: absolute; left: 100px; top: 170px; width: 440px;
  }
  .brand-square {
    width: 110px; height: 110px; background: var(--navy);
    margin-left: 4px; margin-bottom: 40px;
  }
  .brand-name {
    font-family: "Cinzel", serif; font-weight: 700; color: var(--navy);
    line-height: 1.05;
  }
  .brand-name .line-main { display: block; font-size: 62px; letter-spacing: 1px; }
  .brand-name .line-sub { display: block; font-size: 29px; letter-spacing: 1px; margin-top: 6px; }
  .person-name {
    position: absolute; left: 560px; top: 80px;
    font-family: "Cinzel", serif; font-weight: 500;
    font-size: 42px; color: var(--navy); letter-spacing: 1px;
  }
  .contact-list { position: absolute; left: 552px; top: 160px; width: 498px; list-style: none; }
  .contact-item { display: flex; align-items: stretch; margin-bottom: 8px; }
  .contact-icon {
    flex: 0 0 32px; height: 32px; margin-right: 8px;
    display: flex; align-items: center; justify-content: center;
  }
  .contact-band {
    flex: 1; padding: 2px 14px;
    font-family: "Crimson Text", serif; font-size: 25px; line-height: 30px;
    color: var(--ink-light);
  }
  .is-tan .contact-icon, .is-tan .contact-band { background: var(--tan); }
  .is-orange .contact-icon, .is-orange .contact-band { background: var(--orange); }
  .is-brick .contact-icon, .is-brick .contact-band { background: var(--brick); }
  .is-navy .contact-icon, .is-navy .contact-band { background: var(--navy); }
</style>
</head>
<body>
  <div class="card">
    <div class="room-backdrop" role="img" aria-label="Faint line illustration of a furnished living room with lounge chair, pendant lamp and window"></div>

    <div class="brand">
      <div class="brand-square"></div>
      <div class="brand-name">
        <span class="line-main">MERRIWELL</span>
        <span class="line-sub">INTERIOR DESIGNS</span>
      </div>
    </div>

    <div class="person-name">Dana Merriwell</div>

    <ul class="contact-list">
      <li class="contact-item is-tan">
        <span class="contact-icon">
          <svg width="18" height="18" viewBox="0 0 24 24" aria-hidden="true"><path fill="#fff" d="M6.6 10.8a15 15 0 0 0 6.6 6.6l2.2-2.2a1 1 0 0 1 1-.25 11.4 11.4 0 0 0 3.6.57 1 1 0 0 1 1 1V20a1 1 0 0 1-1 1A17 17 0 0 1 3 4a1 1 0 0 1 1-1h3.5a1 1 0 0 1 1 1c0 1.25.2 2.45.57 3.57a1 1 0 0 1-.25 1z"/></svg>
        </span>
        <span class="contact-band">(555) 214-0387</span>
      </li>
      <li class="contact-item is-orange">
        <span class="contact-icon">
          <svg width="18" height="18" viewBox="0 0 24 24" aria-hidden="true"><rect x="3" y="6" width="18" height="12" fill="none" stroke="#fff" stroke-width="2"/><path d="M3 6l9 7 9-7" fill="none" stroke="#fff" stroke-width="2"/></svg>
        </span>
        <span class="contact-band">dana@merriwelldesigns.com</span>
      </li>
      <li class="contact-item is-brick">
        <span class="contact-icon">
          <svg width="18" height="18" viewBox="0 0 24 24" aria-hidden="true"><g fill="none" stroke="#fff" stroke-width="1.8"><circle cx="12" cy="12" r="9"/><ellipse cx="12" cy="12" rx="4" ry="9"/><path d="M3 12h18M5 7h14M5 17h14"/></g></svg>
        </span>
        <span class="contact-band">www.merriwelldesigns.com</span>
      </li>
      <li class="contact-item is-navy">
        <span class="contact-icon">
          <svg width="18" height="18" viewBox="0 0 24 24" aria-hidden="true"><path fill="#fff" d="M12 2a7 7 0 0 0-7 7c0 5 7 13 7 13s7-8 7-13a7 7 0 0 0-7-7zm0 9.5A2.5 2.5 0 1 1 12 6.5a2.5 2.5 0 0 1 0 5z"/></svg>
        </span>
        <span class="contact-band">4821 W Linden Ct.<br>Fairbury, KS 66990</span>
      </li>
    </ul>
  </div>
</body>
</html>
```